Automotive Brand Survey Online

Hi guys, we are looking for a freelancer who can design User Interface design (UI) for a survey-online website layout. <br/><br/>For the content, there are question, choices, back and next buttons - as if you are designing a survey website.<br/><br/>There are 5 main contents of the website consists of:<br/>1. Single-answer question<br/>2. Yes/No-answer question<br/>3. Net Promoter Score (NPS) or 1-5 scale question<br/>4. Open-end question<br/>5. Thank you page when finish survey<br/><br/>Here is the demo and more description<br/>https://demo.quorvel.link/survey/
Target Market(s)
Car Owner
Industry/Entity Type
Automotive
Number of Pages Required
1 page

```html
<!DOCTYPE html>
<html lang="en">
<head>
<meta charset="utf-8">
<title>Kaireo Owner Survey</title>
<link rel="stylesheet" href="https://fonts.googleapis.com/css2?family=Lato:wght@400;700;900&display=swap">
<style>
  :root {
    --bg-deep: #050506;
    --bg-mid: #1a1a1c;
    --text: #ffffff;
    --muted: #e6e6e6;
    --step-ring: #ffffff;
    --step-fill: #0c0c0e;
    --step-done: #3e4258;
    --card-border: #6e6e70;
    --icon: #585c70;
    --back: #5b5b5c;
    --next: #8a3940;
  }
  * { box-sizing: border-box; margin: 0; padding: 0; }
  html, body { width: 1200px; height: 738px; overflow: hidden; background: var(--bg-deep); }
  body { font-family: "Lato", Arial, sans-serif; color: var(--text); }
  .survey-page { position: relative; width: 1200px; height: 738px; overflow: hidden; }
  .hero-backdrop {
    position: absolute; inset: 0;
    background:
      radial-gradient(ellipse 360px 300px at 700px 360px, #2b2b2d 0%, #18181a 55%, transparent 100%),
      radial-gradient(ellipse 700px 520px at 640px 380px, #141416 0%, var(--bg-deep) 100%);
  }
  .brand {
    position: absolute; left: 74px; top: 62px;
    display: flex; align-items: center; gap: 10px;
    font-weight: 900; font-size: 28px; letter-spacing: 1px; color: var(--text);
  }
  .brand-dot { width: 26px; height: 26px; border-radius: 50%; background: var(--text); }

  .progress { position: absolute; left: 475px; top: 68px; width: 660px; height: 70px; }
  .progress-label { position: absolute; left: 0; top: 15px; font-size: 14px; font-weight: 700; letter-spacing: .3px; }
  .progress-track { position: absolute; top: 0; left: 0; }
  .step-pct { position: absolute; top: 51px; width: 60px; margin-left: -30px; text-align: center; font-size: 14px; font-weight: 700; }

  .question-card {
    position: absolute; top: 245px; width: 336px; height: 219px;
    padding: 42px 0 0 25px;
  }
  .question-card.is-active { border: 3px solid var(--card-border); border-radius: 13px; padding: 39px 0 0 22px; }
  .question-title { display: flex; gap: 9px; font-size: 17.5px; font-weight: 700; line-height: 27px; }
  .question-title svg { flex: none; margin-top: 6px; }
  .question-text { max-width: 262px; }
  .choices { display: grid; grid-template-columns: 147px 147px; row-gap: 24px; margin-top: 16px; }
  .choice { display: flex; align-items: center; gap: 14px; font-size: 14px; color: var(--muted); }
  .choice-box { width: 17px; height: 17px; border: 2px solid var(--text); }

  .nav-btn {
    position: absolute; top: 527px; width: 181px; height: 55px; border-radius: 28px;
    display: flex; align-items: center; justify-content: center; gap: 12px;
    font-size: 17.5px; font-weight: 900; color: var(--text); letter-spacing: .3px;
  }
  .nav-back { left: 405px; background: var(--back); }
  .nav-next { left: 614px; background: var(--next); }

  .copyright { position: absolute; top: 674px; left: 0; width: 1200px; text-align: center; font-size: 12.5px; color: var(--muted); }
</style>
</head>
<body>
<main class="survey-page">
  <div class="hero-backdrop" role="img" aria-label="Dark close-up photograph of a car steering wheel centre"></div>

  <div class="brand"><span class="brand-dot"></span>KAIREO</div>

  <div class="progress">
    <span class="progress-label">PROGRESS BAR</span>
    <svg class="progress-track" width="660" height="50" viewBox="0 0 660 50">
      <line x1="174" y1="23" x2="254" y2="23" stroke="#fff" stroke-width="3"/>
      <line x1="174" y1="23" x2="220" y2="23" stroke="var(--step-done)" stroke-width="3"/>
      <line x1="293" y1="23" x2="373" y2="23" stroke="#fff" stroke-width="3"/>
      <line x1="412" y1="23" x2="492" y2="23" stroke="#fff" stroke-width="3"/>
      <line x1="531" y1="23" x2="611" y2="23" stroke="#fff" stroke-width="3"/>
      <circle cx="154" cy="23" r="19" fill="#fff" stroke="var(--step-done)" stroke-width="3"/>
      <path d="M146 23 l5 5 l10 -10" fill="none" stroke="var(--step-done)" stroke-width="3.5"/>
      <g fill="var(--step-fill)" stroke="#fff" stroke-width="2.5">
        <circle cx="273" cy="23" r="19"/><circle cx="392" cy="23" r="19"/>
        <circle cx="511" cy="23" r="19"/><circle cx="630" cy="23" r="19"/>
      </g>
      <g fill="#fff" font-family="Lato, Arial, sans-serif" font-size="19" font-weight="700" text-anchor="middle">
        <text x="273" y="30">2</text><text x="392" y="30">3</text>
        <text x="511" y="30">4</text><text x="630" y="30">5</text>
      </g>
    </svg>
    <span class="step-pct" style="left:154px">0%</span>
    <span class="step-pct" style="left:273px">20%</span>
    <span class="step-pct" style="left:392px">40%</span>
    <span class="step-pct" style="left:511px">80%</span>
    <span class="step-pct" style="left:630px">100%</span>
  </div>

  <section class="question-card is-active" style="left:72px">
    <h2 class="question-title"><svg width="16" height="16" viewBox="0 0 16 16"><circle cx="8" cy="8" r="8" fill="var(--icon)"/><path d="M4.5 8 l2.5 2.5 l4.5 -4.5" fill="none" stroke="#0b0b0c" stroke-width="2"/></svg><span class="question-text">Fusce ut ipsum a libero cursus vitae ultricies?</span></h2>
    <div class="choices">
      <label class="choice"><span class="choice-box"></span>Cras finibus</label>
      <label class="choice"><span class="choice-box"></span>Cras finibus</label>
      <label class="choice"><span class="choice-box"></span>Cras finibus</label>
      <label class="choice"><span class="choice-box"></span>Cras finibus</label>
    </div>
  </section>

  <section class="question-card" style="left:416px">
    <h2 class="question-title"><svg width="16" height="16" viewBox="0 0 16 16"><circle cx="8" cy="8" r="8" fill="var(--icon)"/><path d="M4.5 8 l2.5 2.5 l4.5 -4.5" fill="none" stroke="#0b0b0c" stroke-width="2"/></svg><span class="question-text">Fusce ut ipsum a libero cursus vitae ultricies?</span></h2>
    <div class="choices">
      <label class="choice"><span class="choice-box"></span>Cras finibus</label>
      <label class="choice"><span class="choice-box"></span>Cras finibus</label>
      <label class="choice"><span class="choice-box"></span>Cras finibus</label>
      <label class="choice"><span class="choice-box"></span>Cras finibus</label>
    </div>
  </section>

  <section class="question-card" style="left:776px">
    <h2 class="question-title"><svg width="16" height="16" viewBox="0 0 16 16"><circle cx="8" cy="8" r="8" fill="var(--icon)"/><path d="M4.5 8 l2.5 2.5 l4.5 -4.5" fill="none" stroke="#0b0b0c" stroke-width="2"/></svg><span class="question-text">Fusce ut ipsum a libero cursus vitae ultricies?</span></h2>
    <div class="choices">
      <label class="choice"><span class="choice-box"></span>Cras finibus</label>
      <label class="choice"><span class="choice-box"></span>Cras finibus</label>
      <label class="choice"><span class="choice-box"></span>Cras finibus</label>
      <label class="choice"><span class="choice-box"></span>Cras finibus</label>
    </div>
  </section>

  <a class="nav-btn nav-back"><svg width="22" height="14" viewBox="0 0 22 14"><path d="M8 1 L2 7 L8 13 M18 1 L12 7 L18 13" fill="none" stroke="#fff" stroke-width="2.5"/></svg>BACK</a>
  <a class="nav-btn nav-next">NEXT<svg width="22" height="14" viewBox="0 0 22 14"><path d="M4 1 L10 7 L4 13 M14 1 L20 7 L14 13" fill="none" stroke="#fff" stroke-width="2.5"/></svg></a>

  <footer class="copyright">Copyright © 2020. Company Name. All Right Reserved</footer>
</main>
</body>
</html>
```